Visitenkarten-Design für eine Privatpraxis für Physiotherapie
Zielgruppe
Privatpraxis für Physiotherapie
Aufgabenstellung
----- siehe Ausschreibung ------

```html
<!DOCTYPE html>
<html lang="de">
<head>
<meta charset="utf-8">
<title>Jonas Wehrbeck – Visitenkarten</title>
<link rel="stylesheet" href="https://fonts.googleapis.com/css2?family=Montserrat:wght@400;500;700;800&display=swap">
<style>
  :root {
    --bg: #e9eaec;
    --card: #ffffff;
    --gold: #c9a524;
    --red: #e04a2c;
    --ink: #2c2c2e;
    --muted: #4a4a4c;
    --line: #2c2c2e;
  }
  * { box-sizing: border-box; margin: 0; padding: 0; }
  html, body { width: 1200px; height: 721px; overflow: hidden; }
  body {
    background: var(--bg);
    font-family: "Montserrat", Arial, sans-serif;
    color: var(--ink);
    position: relative;
  }
  .card {
    position: absolute;
    top: 200px;
    width: 520px;
    height: 320px;
    background: var(--card);
    box-shadow: 0 10px 28px rgba(0,0,0,.12);
    overflow: hidden;
  }
  .card--schedule { left: 50px; }
  .card--appointment { left: 630px; }

  .accent-bar { position: absolute; background: var(--red); height: 8px; width: 110px; }
  .accent-bar--top { top: 0; right: 0; }
  .accent-bar--bottom { bottom: 0; left: 0; }

  .brand { position: absolute; display: flex; align-items: center; gap: 12px; }
  .brand__dot { width: 34px; height: 34px; border-radius: 50%; background: var(--gold); flex: none; }
  .brand__name { font-weight: 700; font-size: 17px; color: var(--gold); letter-spacing: .04em; text-transform: uppercase; line-height: 1; }
  .brand__tagline { font-size: 9px; color: var(--red); font-weight: 500; letter-spacing: .06em; margin-top: 4px; }

  /* schedule card */
  .card--schedule .brand { top: 26px; left: 34px; }
  .holder-name { position: absolute; top: 84px; left: 34px; font-weight: 800; font-size: 24px; letter-spacing: .02em; text-transform: uppercase; }
  .schedule { position: absolute; top: 128px; left: 34px; width: 300px; }
  .schedule__title { font-weight: 700; font-size: 13px; letter-spacing: .06em; text-transform: uppercase; padding-bottom: 6px; border-bottom: 1.5px solid var(--line); width: 190px; margin-bottom: 10px; }
  .schedule__row { display: flex; font-size: 11px; margin-bottom: 8px; line-height: 1.35; }
  .schedule__day { width: 110px; text-transform: uppercase; letter-spacing: .04em; }
  .schedule__times { color: var(--muted); }
  .contact { position: absolute; top: 128px; right: 30px; width: 150px; font-size: 10px; font-style: normal; line-height: 1.6; color: var(--muted); border-top: 1.5px solid var(--line); padding-top: 8px; }

  /* appointment card */
  .card--appointment .brand { top: 30px; left: 34px; }
  .appointment-band { position: absolute; top: 92px; left: 0; right: 0; height: 52px; background: var(--gold); display: flex; align-items: center; padding-left: 34px; }
  .appointment-band__label { color: #fff; font-weight: 800; font-size: 24px; letter-spacing: .05em; text-transform: uppercase; }
  .form { position: absolute; top: 168px; left: 34px; right: 40px; }
  .form__field { display: flex; align-items: flex-end; gap: 14px; margin-bottom: 20px; }
  .form__label { width: 54px; font-size: 12px; letter-spacing: .08em; text-transform: uppercase; }
  .form__line { flex: 1; border-bottom: 1.5px solid var(--line); height: 14px; }
</style>
</head>
<body>

<section class="card card--schedule" aria-label="Übungsplan-Karte">
  <span class="accent-bar accent-bar--top"></span>
  <span class="accent-bar accent-bar--bottom"></span>
  <div class="brand">
    <span class="brand__dot"></span>
    <div>
      <div class="brand__name">Jonas Wehrbeck</div>
      <div class="brand__tagline">Privatpraxis für Physiotherapie</div>
    </div>
  </div>
  <h1 class="holder-name">Jonas Wehrbeck</h1>
  <div class="schedule">
    <h2 class="schedule__title">Übungsplan</h2>
    <div class="schedule__row"><span class="schedule__day">Montag</span><span class="schedule__times">07:30 Uhr – 11:30 Uhr<br>14:00 Uhr – 17:00 Uhr</span></div>
    <div class="schedule__row"><span class="schedule__day">Dienstag</span><span class="schedule__times">07:30 Uhr – 11:30 Uhr<br>14:00 Uhr – 17:00 Uhr</span></div>
    <div class="schedule__row"><span class="schedule__day">Donnerstag</span><span class="schedule__times">07:30 Uhr – 11:30 Uhr<br>14:00 Uhr – 17:00 Uhr</span></div>
  </div>
  <address class="contact">
    Privatpraxis für Physiotherapie<br>
    Birkenallee 4<br>
    01010 Horstfeld<br>
    Tel. 0000 123456
  </address>
</section>

<section class="card card--appointment" aria-label="Terminkarte">
  <span class="accent-bar accent-bar--top"></span>
  <span class="accent-bar accent-bar--bottom"></span>
  <div class="brand">
    <span class="brand__dot"></span>
    <div>
      <div class="brand__name">Jonas Wehrbeck</div>
      <div class="brand__tagline">Privatpraxis für Physiotherapie</div>
    </div>
  </div>
  <div class="appointment-band"><span class="appointment-band__label">Appointment</span></div>
  <div class="form">
    <div class="form__field"><span class="form__label">Name</span><span class="form__line"></span></div>
    <div class="form__field"><span class="form__label">Date</span><span class="form__line"></span></div>
    <div class="form__field"><span class="form__label">Time</span><span class="form__line"></span></div>
  </div>
</section>

</body>
</html>
```